Website for vegan focused blog

A website is needed so that I can launch my new blog in Dubai. It will be mainly vegan focused but also lifestyle based. Wordpress based- i started to build a site on Wordpress but design is not my forte ;)
Main content on the site will be; my recipes, reviews of products/restaurants, lifestyle posts and travel.
For this I ask for a homepage design, a recipe design page that includes a recipe card and a generic page for posts that can show pictures and videos. Also a contact me page.
Main headers should be: Home, Recipes and happy for suggestions.
Must look clean and neat but appealing, happy for minimalist look. I like pink and grey colours. Must be Wordpress compatible.
Have attached a couple of example posts for reference
Must have social links etc.
name of blog is: Marnie on the dunes
Other blogs I like are: https://tidyskillet.example/ https://shebrightens.example/ https://shebrightens.example/ https://www.ohladycakes.com/https://figsforsupper.example/ https://tessaborlow.example/

Target Market(s)

Residents in the UAE. General individuals interested in vegan meals, plant based nutrition, travel and reviews.

Number of Pages Required

4 page

Colors
eea4c8
eda3c7
f9d9e8
dbdbdb
aaaaaa
d5d5d5

Requirements
Must have
• Recipe page- must include recipe card plug in option
• Social media integration
• Email sign ups

```html
<!DOCTYPE html>
<html lang="en">
<head>
<meta charset="utf-8">
<title>Marnie on the dunes</title>
<link href="https://fonts.googleapis.com/css2?family=Poppins:wght@300;400;500;600;700&family=Roboto:wght@500;700;900&display=swap" rel="stylesheet">
<style>
:root{
  --pink:#eea4c8;
  --pink-deep:#e58ab8;
  --pink-soft:#f9d9e8;
  --grey-line:#dbdbdb;
  --grey-mid:#aaaaaa;
  --grey-light:#d5d5d5;
  --page:#f6f6f6;
  --ink:#1d1d1d;
  --body:#555555;
  --footer:#0b0b0b;
  --white:#ffffff;
  --star:#e8a13a;
}
*{box-sizing:border-box;margin:0;padding:0}
html,body{width:1200px;height:3782px;overflow:hidden}
body{position:relative;background:var(--page);font-family:"Poppins",sans-serif;color:var(--ink)}
.abs{position:absolute}
svg{display:block}

/* header */
.site-header{left:0;top:0;width:1200px;height:88px;background:var(--pink)}
.brand{left:143px;top:22px;font-size:30px;font-weight:500;color:var(--white);letter-spacing:.5px}
.main-nav{right:145px;top:0;height:88px;display:flex;align-items:center;gap:30px}
.main-nav a{color:var(--white);text-decoration:none;font-size:19px;font-weight:500}
.search-btn{width:30px;height:30px;border:2px solid var(--white);border-radius:50%;display:flex;align-items:center;justify-content:center}

/* hero */
.hero{left:0;top:88px;width:1200px;height:562px;background:linear-gradient(100deg,#cfc3bb 0%,#b9a79c 30%,#e9e3dc 55%,#f2ecdf 75%,#d6c07a 100%)}
.hero-title{left:545px;top:152px;width:400px;text-align:center;font-family:"Roboto",sans-serif;font-weight:700;font-size:52px;line-height:60px;color:var(--white)}
.hero-btn{left:681px;top:306px;width:129px;height:39px;border:2px solid var(--white);color:var(--white);font-size:14px;font-weight:600;display:flex;align-items:center;justify-content:center;background:rgba(0,0,0,.08)}
.hero-arrow{top:238px;width:32px;height:32px;border-radius:50%;background:#2b2b2b;display:flex;align-items:center;justify-content:center}

/* about */
.about-photo{left:143px;top:713px;width:415px;height:330px;background:linear-gradient(180deg,#d8a56f 0%,#8a6a57 45%,#3d3a3e 70%,#1f2327 100%)}
.about-box{left:558px;top:713px;width:497px;height:360px;background:var(--pink-soft);padding:30px 38px}
.about-box h2{font-family:"Roboto",sans-serif;font-weight:900;font-size:31px;letter-spacing:.5px}
.about-rule{width:58px;height:3px;background:var(--ink);margin:14px 0 20px}
.about-box p{font-size:13px;line-height:27px;color:#333}
.outline-btn{display:inline-flex;align-items:center;justify-content:center;height:32px;padding:0 10px;border:2px solid var(--ink);font-size:13px;font-weight:600;margin-top:12px;background:transparent}

/* section heads */
.sec-head{font-size:28px;font-weight:500;letter-spacing:.5px}
.sec-head span{color:var(--pink-deep);font-weight:700}
.side-head{font-family:"Roboto",sans-serif;font-weight:900;font-size:28px}
.side-head span{color:var(--pink-deep)}

/* meta */
.meta{display:flex;gap:22px;font-size:12px;color:var(--pink-deep);align-items:center}
.meta i{font-style:normal;display:inline-flex;align-items:center;gap:6px}
.meta i+i{border-left:1px solid var(--grey-line);padding-left:18px}

/* big post */
.big-img{left:143px;width:652px;height:268px}
.big-card{left:165px;width:607px;height:170px;background:var(--white);border:1px solid var(--grey-line);box-shadow:0 2px 6px rgba(0,0,0,.08);padding:18px 26px;text-align:center}
.big-card h3{font-size:15px;font-weight:500;margin-bottom:14px}
.big-card .meta{justify-content:center;margin-bottom:12px}
.big-card p{font-size:11.5px;line-height:20px;color:var(--body)}

/* list post */
.list-post{left:143px;width:652px;height:222px;background:var(--white);border:1px solid var(--grey-line)}
.list-img{left:0;top:0;width:287px;height:222px}
.list-body{left:310px;top:20px;width:325px}
.list-body h3{font-size:15px;font-weight:500;line-height:22px;margin-bottom:14px}
.list-body .meta{margin-bottom:12px}
.list-body p{font-size:11.5px;line-height:20px;color:var(--body)}
.read-more{font-size:10px;color:var(--pink-deep);letter-spacing:.5px;margin-top:12px;display:block}

/* sidebar recipes */
.recipe{left:838px;width:217px}
.recipe-img{width:217px;height:133px}
.recipe .meta{font-size:11px;gap:14px;margin:20px 0 12px}
.recipe .meta i+i{padding-left:12px}
.recipe h4{font-size:14px;font-weight:400;line-height:20px}

/* community */
.member{left:838px;display:flex;gap:16px;align-items:center}
.avatar{width:80px;height:80px;border-radius:50%;border:3px solid #2a2a2a}
.member-text{font-size:12px;line-height:17px}
.stars{display:flex;gap:2px;margin-top:3px}

/* follow */
.follow-grid{left:838px;top:2827px;display:grid;grid-template-columns:repeat(3,71px);gap:2px}
.tile{height:72px;color:var(--white);display:flex;flex-direction:column;align-items:center;justify-content:flex-end;padding-bottom:6px;font-size:11px;line-height:13px;text-align:center}
.tile b{width:20px;height:20px;border-radius:50%;background:rgba(255,255,255,.85);margin-bottom:6px}

/* pagination */
.pager{left:143px;top:3278px;display:flex;gap:6px}
.pager span{height:22px;min-width:22px;padding:0 7px;border:1px solid var(--grey-mid);background:var(--white);font-size:11px;display:flex;align-items:center;justify-content:center}

/* footer */
.site-footer{left:0;top:3360px;width:1200px;height:422px;background:var(--footer);color:var(--white)}
.foot-head{font-family:"Roboto",sans-serif;font-weight:700;font-size:22px;letter-spacing:.5px}
.contact-row{display:flex;gap:18px;font-size:13px;line-height:22px}
.signup-field{width:298px;height:40px;border-radius:20px;background:var(--white);display:flex;align-items:center;justify-content:space-between;padding-left:18px;color:#777;font-size:12px}
.signup-btn{height:40px;padding:0 22px;border-radius:20px;background:var(--pink);color:var(--white);font-weight:600;font-size:13px;display:flex;align-items:center}
.social-dots{display:flex;gap:6px}
.social-dots span{width:24px;height:24px;border:1px solid var(--white);border-radius:50%}
.quick-links{font-size:14px;line-height:30px;list-style:none}
.copyright{left:0;top:3730px;width:1200px;text-align:center;font-size:14px}
</style>
</head>
<body>

<header class="site-header abs">
  <div class="brand abs">Marnie on the dunes</div>
  <nav class="main-nav abs">
    <a href="#">Home</a><a href="#">Recipe</a><a href="#">Blog</a><a href="#">Contact</a>
    <span class="search-btn"><svg width="14" height="14" viewBox="0 0 14 14"><circle cx="6" cy="6" r="4.2" fill="none" stroke="#fff" stroke-width="2"/><path d="M9 9l4 4" stroke="#fff" stroke-width="2"/></svg></span>
  </nav>
</header>

<section class="hero abs" role="img" aria-label="Smiling woman holding two halves of dragon fruit over her eyes beside a fruit-filled jar and pineapples"></section>
<div class="hero-title abs">MARNIE ON<br>THE DUNES</div>
<div class="hero-btn abs">READ MORE</div>
<div class="hero-arrow abs" style="left:98px"><svg width="12" height="12" viewBox="0 0 12 12"><path d="M8 1L3 6l5 5" fill="none" stroke="#fff" stroke-width="2"/></svg></div>
<div class="hero-arrow abs" style="left:1068px"><svg width="12" height="12" viewBox="0 0 12 12"><path d="M4 1l5 5-5 5" fill="none" stroke="#fff" stroke-width="2"/></svg></div>

<div class="about-photo abs" role="img" aria-label="Person standing on a rocky beach at sunset"></div>
<section class="about-box abs">
  <h2>ABOUT ME</h2>
  <div class="about-rule"></div>
  <p>I'm Marnie. Born and raised in the UK but been living in Dubai since 2012. I have always had a love for animals after growing up around all sorts; from dogs, horses, cats, hamsters, rabbits, the odd injured pigeon or hedgehog in the house and even scary cockerels to name a few! I am a massive foodie, love travelling the world, new adventures, the beach and working</p>
  <span class="outline-btn">READ MORE</span>
</section>

<h2 class="sec-head abs" style="left:143px;top:1140px">MOST <span>POPULAR</span></h2>
<h2 class="sec-head abs" style="left:838px;top:1140px">LATEST <span>RECIPE</span></h2>

<!-- big posts -->
<div class="big-img abs" style="top:1200px;background:linear-gradient(90deg,#c21f72,#d6488f 60%,#3a3a3a)" role="img" aria-label="Bowl of pink beet soup with radish slices"></div>
<article class="big-card abs" style="top:1425px">
  <h3>Nemo enim ipsam voluptatem quia voluptas sit aspernatur</h3>
  <div class="meta"><i><svg width="11" height="11" viewBox="0 0 11 11"><rect x="1" y="2" width="9" height="8" fill="none" stroke="currentColor"/><path d="M1 4.5h9" stroke="currentColor"/></svg>Jan 25, 2018</i><i><svg width="11" height="11" viewBox="0 0 11 11"><path d="M1 2h9v6H4l-3 2z" fill="none" stroke="currentColor"/></svg>2 comments</i><i><svg width="11" height="11" viewBox="0 0 11 11"><path d="M2 9l1-3 5-5 2 2-5 5z" fill="none" stroke="currentColor"/></svg>by Tomas</i></div>
  <p>Sed ut perspiciatis unde omnis iste natus error sit voluptatem accusantium doloremque laudantium, totam rem aperiam, eaque ipsa quae ab illo inventore veritatis et quasi architecto beatae vitae dicta sunt explicabo. Nemo enim ipsam voluptatem quia voluptas sit aspernatur</p>
</article>

<div class="big-img abs" style="top:1633px;background:linear-gradient(90deg,#2a2a2a,#3d5a2a 45%,#6c8a34 60%,#2a2a2a)" role="img" aria-label="Plate of broccoli and greens with a fork on a dark table"></div>
<article class="big-card abs" style="top:1858px">
  <h3>Nemo enim ipsam voluptatem quia voluptas sit aspernatur</h3>
  <div class="meta"><i><svg width="11" height="11" viewBox="0 0 11 11"><rect x="1" y="2" width="9" height="8" fill="none" stroke="currentColor"/><path d="M1 4.5h9" stroke="currentColor"/></svg>Jan 25, 2018</i><i><svg width="11" height="11" viewBox="0 0 11 11"><path d="M1 2h9v6H4l-3 2z" fill="none" stroke="currentColor"/></svg>2 comments</i><i><svg width="11" height="11" viewBox="0 0 11 11"><path d="M2 9l1-3 5-5 2 2-5 5z" fill="none" stroke="currentColor"/></svg>by Tomas</i></div>
  <p>Sed ut perspiciatis unde omnis iste natus error sit voluptatem accusantium doloremque laudantium, totam rem aperiam, eaque ipsa quae ab illo inventore veritatis et quasi architecto beatae vitae dicta sunt explicabo. Nemo enim ipsam voluptatem quia voluptas sit aspernatur</p>
</article>

<div class="big-img abs" style="top:2066px;background:linear-gradient(90deg,#1f2a22,#43503a 40%,#8a8a80 55%,#2b3a2a)" role="img" aria-label="Hand holding a phone photographing a salad bowl from above"></div>
<article class="big-card abs" style="top:2291px">
  <h3>Nemo enim ipsam voluptatem quia voluptas sit aspernatur</h3>
  <div class="meta"><i><svg width="11" height="11" viewBox="0 0 11 11"><rect x="1" y="2" width="9" height="8" fill="none" stroke="currentColor"/><path d="M1 4.5h9" stroke="currentColor"/></svg>Jan 25, 2018</i><i><svg width="11" height="11" viewBox="0 0 11 11"><path d="M1 2h9v6H4l-3 2z" fill="none" stroke="currentColor"/></svg>2 comments</i><i><svg width="11" height="11" viewBox="0 0 11 11"><path d="M2 9l1-3 5-5 2 2-5 5z" fill="none" stroke="currentColor"/></svg>by Tomas</i></div>
  <p>Sed ut perspiciatis unde omnis iste natus error sit voluptatem accusantium doloremque laudantium, totam rem aperiam, eaque ipsa quae ab illo inventore veritatis et quasi architecto beatae vitae dicta sunt explicabo. Nemo enim ipsam voluptatem quia voluptas sit aspernatur</p>
</article>

<!-- list posts -->
<article class="list-post abs" style="top:2507px">
  <div class="list-img abs" style="background:linear-gradient(135deg,#2f3b2c,#5f7d3c 50%,#cfcfc4)" role="img" aria-label="Hands holding a bowl of leafy salad"></div>
  <div class="list-body abs">
    <h3>Nemo enim ipsam voluptatem quia voluptas sit aspernatur</h3>
    <div class="meta"><i>Jan 25, 2018</i><i>2 comments</i><i>by Tomas</i></div>
    <p>Sed ut perspiciatis unde omnis iste natus error sit voluptatem accusantium doloremque laudantium, totam rem aperiam, eaque ipsa quae ab illo inventore veritatis</p>
    <span class="read-more">READ MORE &gt;&gt;</span>
  </div>
</article>
<article class="list-post abs" style="top:2747px">
  <div class="list-img abs" style="background:linear-gradient(135deg,#2a2a2a,#b5652a 45%,#d99a3c 60%,#3a3a3a)" role="img" aria-label="Filled tacos with vegetables on a dark board"></div>
  <div class="list-body abs">
    <h3>Nemo enim ipsam voluptatem quia voluptas sit aspernatur</h3>
    <div class="meta"><i>Jan 25, 2018</i><i>2 comments</i><i>by Tomas</i></div>
    <p>Sed ut perspiciatis unde omnis iste natus error sit voluptatem accusantium doloremque laudantium, totam rem aperiam, eaque ipsa quae ab illo inventore veritatis</p>
    <span class="read-more">READ MORE &gt;&gt;</span>
  </div>
</article>
<article class="list-post abs" style="top:2987px">
  <div class="list-img abs" style="background:linear-gradient(135deg,#c9b9a8,#9aa86a 45%,#b8563a 65%,#d9cbbb)" role="img" aria-label="Lettuce wrap burger on a light surface"></div>
  <div class="list-body abs">
    <h3>Nemo enim ipsam voluptatem quia voluptas sit aspernatur</h3>
    <div class="meta"><i>Jan 25, 2018</i><i>2 comments</i><i>by Tomas</i></div>
    <p>Sed ut perspiciatis unde omnis iste natus error sit voluptatem accusantium doloremque laudantium, totam rem aperiam, eaque ipsa quae ab illo inventore veritatis</p>
    <span class="read-more">READ MORE &gt;&gt;</span>
  </div>
</article>

<nav class="pager abs"><span>Prev</span><span>1</span><span>2</span><span>3</span><span>4</span><span>5</span><span>6</span><span>...</span><span>22</span><span>Next</span></nav>

<!-- sidebar recipes -->
<div class="recipe abs" style="top:1200px">
  <div class="recipe-img" style="background:linear-gradient(135deg,#7a9a3c,#c8452f 50%,#d89a6a)" role="img" aria-label="Assorted fresh vegetables and fruit"></div>
  <div class="meta"><i>Jan 25, 2018</i><i>2 comments</i></div>
  <h4>Nemo enim ipsam volupta voluptas sit aspernatur</h4>
  <span class="read-more">READ MORE &gt;&gt;</span>
</div>
<div class="recipe abs" style="top:1465px">
  <div class="recipe-img" style="background:linear-gradient(135deg,#6d5a4a,#b8232e 50%,#7a8c3a)" role="img" aria-label="Heart-shaped dish of fruit and vegetables"></div>
  <div class="meta"><i>Jan 25, 2018</i><i>2 comments</i></div>
  <h4>Nemo enim ipsam volupta voluptas sit aspernatur</h4>
  <span class="read-more">READ MORE &gt;&gt;</span>
</div>
<div class="recipe abs" style="top:1730px">
  <div class="recipe-img" style="background:radial-gradient(circle,#f1efe4 20%,#c9b48a 45%,#5a6a4a 80%)" role="img" aria-label="Bowl of salad with greens seen from above"></div>
  <div class="meta"><i>Jan 25, 2018</i><i>2 comments</i></div>
  <h4>Nemo enim ipsam volupta voluptas sit aspernatur</h4>
  <span class="read-more">READ MORE &gt;&gt;</span>
</div>
<div class="recipe abs" style="top:1998px">
  <div class="recipe-img" style="background:linear-gradient(135deg,#3a2a1e,#8a4a22 50%,#4a3322)" role="img" aria-label="Roasted vegetables on a baking tray"></div>
  <div class="meta"><i>Jan 25, 2018</i><i>2 comments</i></div>
  <h4>Nemo enim ipsam volupta voluptas sit aspernatur</h4>
  <span class="read-more">READ MORE &gt;&gt;</span>
</div>

<h2 class="side-head abs" style="left:838px;top:2282px">COMMUNITY</h2>
<div class="member abs" style="top:2342px"><div class="avatar" style="background:#6a5a50" role="img" aria-label="Member portrait"></div><div class="member-text">Rosa Lindqvist<br>Sed ut perspiciatis<div class="stars"><svg width="60" height="10" viewBox="0 0 60 10"><g fill="var(--star)"><circle cx="5" cy="5" r="4"/><circle cx="17" cy="5" r="4"/><circle cx="29" cy="5" r="4"/></g><g fill="var(--grey-light)"><circle cx="41" cy="5" r="4"/><circle cx="53" cy="5" r="4"/></g></svg></div></div></div>
<div class="member abs" style="top:2445px"><div class="avatar" style="background:#b98a6a" role="img" aria-label="Member portrait"></div><div class="member-text">Rosa Lindqvist<br>Sed ut perspiciatis<div class="stars"><svg width="60" height="10" viewBox="0 0 60 10"><g fill="var(--star)"><circle cx="5" cy="5" r="4"/><circle cx="17" cy="5" r="4"/><circle cx="29" cy="5" r="4"/></g><g fill="var(--grey-light)"><circle cx="41" cy="5" r="4"/><circle cx="53" cy="5" r="4"/></g></svg></div></div></div>
<div class="member abs" style="top:2548px"><div class="avatar" style="background:#9a7a66" role="img" aria-label="Member portrait"></div><div class="member-text">Rosa Lindqvist<br>Sed ut perspiciatis<div class="stars"><svg width="60" height="10" viewBox="0 0 60 10"><g fill="var(--star)"><circle cx="5" cy="5" r="4"/><circle cx="17" cy="5" r="4"/><circle cx="29" cy="5" r="4"/></g><g fill="var(--grey-light)"><circle cx="41" cy="5" r="4"/><circle cx="53" cy="5" r="4"/></g></svg></div></div></div>
<div class="member abs" style="top:2651px"><div class="avatar" style="background:#a87a5e" role="img" aria-label="Member portrait"></div><div class="member-text">Rosa Lindqvist<br>Sed ut perspiciatis<div class="stars"><svg width="60" height="10" viewBox="0 0 60 10"><g fill="var(--star)"><circle cx="5" cy="5" r="4"/><circle cx="17" cy="5" r="4"/><circle cx="29" cy="5" r="4"/></g><g fill="var(--grey-light)"><circle cx="41" cy="5" r="4"/><circle cx="53" cy="5" r="4"/></g></svg></div></div></div>

<h2 class="side-head abs" style="left:838px;top:2765px">FOLLOW <span>US</span></h2>
<div class="follow-grid abs">
  <div class="tile" style="background:#6f6f6f"><b></b>68,876<br>Fans</div>
  <div class="tile" style="background:var(--pink)"><b></b>65<br>Followers</div>
  <div class="tile" style="background:var(--pink-deep)"><b></b>8,961<br>Followers</div>
  <div class="tile" style="background:#8a8a8a"><b></b>68,876<br>Fans</div>
  <div class="tile" style="background:#c46c98"><b></b>65<br>Followers</div>
  <div class="tile" style="background:#9e9e9e"><b></b>8,961<br>Followers</div>
</div>

<footer class="site-footer abs">
  <h3 class="foot-head abs" style="left:143px;top:62px">CONTACT US</h3>
  <div class="abs" style="left:143px;top:118px;width:260px">
    <div class="contact-row"><svg width="14" height="18" viewBox="0 0 14 18"><path d="M7 17S1 10 1 6.5a6 6 0 0112 0C13 10 7 17 7 17z" fill="none" stroke="#fff" stroke-width="1.5"/><circle cx="7" cy="6.5" r="2" fill="#fff"/></svg><span>Marnie on the dunes<br>42 Larkmoor Lane, Fenwick<br>Bay 20417</span></div>
    <div class="contact-row" style="margin-top:14px"><svg width="16" height="16" viewBox="0 0 16 16"><path d="M3 1l3 3-2 2c1 2 3 4 6 6l2-2 3 3-2 2C7 15 1 9 1 3z" fill="none" stroke="#fff" stroke-width="1.3"/></svg><span>Phone : 555-014-2290</span></div>
    <div class="contact-row" style="margin-top:14px"><svg width="16" height="14" viewBox="0 0 16 14"><rect x="1" y="2" width="14" height="10" fill="none" stroke="#fff" stroke-width="1.3"/><path d="M1 2l7 6 7-6" fill="none" stroke="#fff" stroke-width="1.3"/></svg><span>Email : hello@marnieonthedunes.example</span></div>
  </div>
  <h3 class="foot-head abs" style="left:467px;top:62px">SIGN UP TO RECEIVE EMAIL</h3>
  <p class="abs" style="left:467px;top:115px;width:310px;font-size:12px;line-height:22px">Excepteur sint occaecat cupidatat non proident, sunt in culpa qui Nemo enim ipsam voluptatem</p>
  <div class="signup-field abs" style="left:467px;top:180px">Enter Email<span class="signup-btn">SUBSCRIBE</span></div>
  <div class="social-dots abs" style="left:475px;top:248px"><span></span><span></span><span></span><span></span></div>
  <h3 class="foot-head abs" style="left:905px;top:62px">QUICK LINKS</h3>
  <ul class="quick-links abs" style="left:910px;top:112px"><li>Home</li><li>Recipe</li><li>Blog</li><li>contact</li></ul>
</footer>
<p class="copyright abs" style="color:#fff">Copyright © Marnie on the dunes 2018. All rights reserved. | Privacy Policy</p>

</body>
</html>
```